Animal Hospital Business Cards

Make a business card look like the attached example

*Use the same blue/black coloring
*Fenbrook Hollow Animal Hospital (instead of mobile pet rounds)
*Emergency Services (instead of tri-county care center)
*House Calls (instead of open 7 days by appointment)
*Change address to 1873 Tilden Marsh Rd Loveland, OH 45140
*Open 7 days a week (instead of emergency service)
*Add the website www.fenbrookhollowanimalhospital.example

On the back...
*instead of the text outlined in red, just white
*instead of the light blue, try your best to make it just like the blue and black on the front side of the card
*Delete "designed and printed by Blue Heron Print Co, www.blueheronprintco.example

Requirements
Must have
• look just like the attached example with requested edits/changes

```html
<!DOCTYPE html>
<html lang="en">
<head>
<meta charset="UTF-8">
<title>Fenbrook Hollow Animal Hospital – Business Cards</title>
<link href="https://fonts.googleapis.com/css2?family=Montserrat:wght@400;500;700;800&family=Roboto:wght@700&display=swap" rel="stylesheet">
<style>
  :root {
    --page-bg: #2a2a2a;
    --brand-blue: #4a5d7b;
    --label-blue: #50658a;
    --card-dark: #1f1f1f;
    --card-white: #ffffff;
    --ink: #1a1a1a;
    --light-text: #ffffff;
  }
  * { box-sizing: border-box; margin: 0; padding: 0; }
  html, body { width: 1200px; height: 900px; overflow: hidden; }
  body {
    background: var(--page-bg);
    font-family: "Montserrat", sans-serif;
    position: relative;
  }
  .card {
    position: absolute;
    left: 250px;
    width: 700px;
    height: 400px;
    overflow: hidden;
  }
  /* ---------- appointment side ---------- */
  .appointment-card { top: 35px; background: var(--card-white); color: var(--ink); }
  .appointment-header {
    height: 120px;
    background: var(--brand-blue);
    color: var(--light-text);
    text-align: center;
    padding-top: 22px;
  }
  .appointment-title { font-size: 26px; font-weight: 500; letter-spacing: 1px; }
  .vet-name { font-size: 19px; letter-spacing: 3px; margin-top: 2px; }
  .vet-phone { font-size: 19px; letter-spacing: 3px; margin-top: 2px; }
  .appointment-form { padding: 24px 34px 0; font-size: 20px; letter-spacing: 2px; }
  .form-row { display: flex; align-items: flex-end; margin-bottom: 26px; }
  .fill-line { flex: 1; border-bottom: 1.5px solid var(--ink); margin: 0 8px; height: 22px; }
  .weekday-row { display: flex; justify-content: space-between; margin-bottom: 26px; }
  .weekday { display: flex; align-items: center; gap: 5px; }
  .checkbox { width: 15px; height: 15px; border: 2px solid var(--ink); display: inline-block; }
  .meridiem { font-size: 15px; line-height: 1.05; letter-spacing: 1px; margin-left: 4px; }
  /* ---------- front side ---------- */
  .hospital-card { top: 465px; background: var(--card-dark); color: var(--light-text); }
  .hospital-header {
    height: 108px;
    background: var(--brand-blue);
    text-align: center;
    padding-top: 18px;
  }
  .hospital-name { font-size: 38px; font-weight: 700; }
  .hospital-tagline { font-size: 24px; letter-spacing: 9px; margin-top: 2px; }
  .hospital-body { display: flex; justify-content: space-between; height: 232px; padding: 14px 34px 0; }
  .info-column { width: 250px; }
  .info-column.right { width: 370px; text-align: right; padding-top: 28px; }
  .section-label {
    font-family: "Roboto", sans-serif;
    font-weight: 700;
    font-size: 22px;
    color: var(--label-blue);
  }
  .rule { border-top: 2px solid var(--light-text); margin: 8px 0 6px; }
  .info-text { font-size: 19px; font-weight: 500; line-height: 1.3; white-space: nowrap; }
  .contact-text { font-size: 16px; font-weight: 500; line-height: 1.45; white-space: nowrap; }
  .hospital-footer {
    height: 60px;
    background: var(--brand-blue);
    display: flex;
    align-items: center;
    padding-left: 160px;
    font-size: 30px;
    font-weight: 500;
  }
</style>
</head>
<body>

<section class="card appointment-card">
  <header class="appointment-header">
    <div class="appointment-title">Veterinary Appointment</div>
    <div class="vet-name">Marcus L. Delaney, DVM</div>
    <div class="vet-phone">513.555.0147</div>
  </header>
  <div class="appointment-form">
    <div class="form-row"><span>Your appointment for</span><span class="fill-line"></span><span>is on</span></div>
    <div class="weekday-row">
      <span class="weekday"><span class="checkbox"></span>Mon.</span>
      <span class="weekday"><span class="checkbox"></span>Tues.</span>
      <span class="weekday"><span class="checkbox"></span>Wed.</span>
      <span class="weekday"><span class="checkbox"></span>Thurs.</span>
      <span class="weekday"><span class="checkbox"></span>Fri.</span>
      <span class="weekday"><span class="checkbox"></span>Sat.</span>
    </div>
    <div class="form-row">
      <span>Date</span><span class="fill-line"></span>
      <span>Time</span><span class="fill-line"></span>
      <span class="meridiem">AM<br>PM</span>
    </div>
  </div>
</section>

<section class="card hospital-card">
  <header class="hospital-header">
    <div class="hospital-name">Fenbrook Hollow Animal Hospital</div>
    <div class="hospital-tagline">(instead of mobile pet rounds)</div>
  </header>
  <div class="hospital-body">
    <div class="info-column left">
      <div class="section-label">Emergency Services</div>
      <div class="rule"></div>
      <div class="info-text">instead of<br>tri-county - care - center</div>
      <div class="rule"></div>
      <div class="info-text">1873 Tilden Marsh Rd<br>Loveland, OH 45140</div>
    </div>
    <div class="info-column right">
      <div class="rule"></div>
      <div class="section-label">House Calls</div>
      <div class="rule"></div>
      <div class="info-text">instead of open 7 days<br>By appointment</div>
      <div class="rule"></div>
      <div class="contact-text">(513) 555 0147<br>fenbrookhollowanimalhospital.example</div>
    </div>
  </div>
  <footer class="hospital-footer">Open 7 days a week</footer>
</section>

</body>
</html>
```